Business Card for Makeup Artist

I need a business card designed for my makeup and hair artistry business which is primarily events and weddings focused. The card needs to be sleek, simple, stylish and appealing to women. I would prefer a white background but open to suggestions also. I also love the marble background look. I have attached some example pics. It needs to be a double sided card with logo and/or design on one side and contact details in the centre of the card on the other side. NO LOGO ON BACK. Examples attached.

Target Market(s)

Females age 14-55

Industry/Entity Type

Business

Contact Information for Business Card

Nora Vint
Principal Makeup Artist
P: 0413 925 214
E: nora@lumirabeauty.com.au
W: www.lumirabeauty.com.au

Requirements
Should not have
• No yellow, green, red or blue in the design.

```html
<!DOCTYPE html>
<html lang="en">
<head>
<meta charset="utf-8">
<title>Lumira Makeup Artistry – Business Card</title>
<link rel="stylesheet" href="https://fonts.googleapis.com/css2?family=Didact+Gothic&family=Open+Sans:wght@700&display=swap">
<style>
  :root {
    --stage: #3a3a3a;
    --card-black: #0b0b0b;
    --card-texture-a: #161616;
    --card-texture-b: #202020;
    --gold-dark: #a8703a;
    --gold-light: #e8b77c;
    --white: #ffffff;
    --pink: #e35fd3;
  }
  html, body {
    margin: 0;
    padding: 0;
    width: 1200px;
    height: 947px;
    overflow: hidden;
    background: var(--stage);
  }
  .canvas {
    width: 1200px;
    height: 947px;
    display: flex;
    flex-direction: column;
    align-items: center;
    justify-content: center;
    gap: 47px;
  }
  .card {
    position: relative;
    width: 700px;
    height: 400px;
    background: var(--card-black);
    overflow: hidden;
    box-shadow: 0 10px 30px rgba(0,0,0,0.45);
  }
  .card__texture {
    position: absolute;
    inset: 0;
    background: linear-gradient(135deg, var(--card-texture-a), var(--card-texture-b) 50%, var(--card-texture-a));
  }
  .gold {
    background: linear-gradient(90deg, var(--gold-dark), var(--gold-light) 55%, var(--gold-dark));
  }

  /* Front */
  .front__band {
    position: absolute;
    left: 0;
    right: 0;
    top: 152px;
    height: 96px;
  }
  .front__frame {
    position: absolute;
    left: 160px;
    top: 90px;
    width: 380px;
    height: 220px;
    box-sizing: border-box;
    padding: 6px;
  }
  .front__panel {
    width: 100%;
    height: 100%;
    background: var(--card-black);
    display: flex;
    flex-direction: column;
    align-items: center;
    justify-content: center;
  }

  /* Brand name */
  .brand {
    font-family: "Didact Gothic", sans-serif;
    color: var(--white);
    text-align: center;
    line-height: 1;
  }
  .brand__name {
    font-size: 64px;
    letter-spacing: 2px;
  }
  .brand__tagline {
    margin-top: 8px;
    font-size: 19px;
    letter-spacing: 3px;
  }

  /* Back */
  .back__header {
    position: absolute;
    left: 0;
    right: 0;
    top: 0;
    height: 170px;
    background: var(--card-black);
  }
  .back__rule {
    position: absolute;
    left: 0;
    right: 0;
    top: 170px;
    height: 8px;
  }
  .back__contact {
    position: absolute;
    left: 0;
    right: 0;
    top: 200px;
    text-align: center;
    color: var(--white);
  }
  .contact__name {
    font-family: "Open Sans", sans-serif;
    font-weight: 700;
    font-size: 26px;
    line-height: 1.3;
    letter-spacing: 1px;
    margin: 0;
  }
  .contact__role {
    font-family: "Open Sans", sans-serif;
    font-weight: 700;
    font-size: 18px;
    line-height: 1.3;
    color: var(--pink);
    margin: 4px 0 22px;
  }
  .contact__phone,
  .contact__links {
    font-family: "Didact Gothic", sans-serif;
    font-size: 18px;
    line-height: 1.3;
    margin: 0 0 14px;
  }
  .contact__divider {
    display: inline-block;
    width: 3px;
    height: 18px;
    background: var(--pink);
    margin: 0 12px;
    vertical-align: -3px;
  }
</style>
</head>
<body>
<main class="canvas">
  <section class="card card--front">
    <div class="card__texture" role="img" aria-label="Dark embossed woven pattern background"></div>
    <div class="front__band gold"></div>
    <div class="front__frame gold">
      <div class="front__panel">
        <div class="brand">
          <div class="brand__name">Lumira</div>
          <div class="brand__tagline">MAKEUP ARTISTRY</div>
        </div>
      </div>
    </div>
  </section>

  <section class="card card--back">
    <div class="card__texture" role="img" aria-label="Dark embossed woven pattern background"></div>
    <div class="back__header"></div>
    <div class="back__rule gold"></div>
    <div class="back__contact">
      <p class="contact__name">NORA VINT</p>
      <p class="contact__role">Principal Makeup Artist</p>
      <p class="contact__phone">0413 925 214</p>
      <p class="contact__links">nora@lumirabeauty.com.au<span class="contact__divider" aria-hidden="true"></span>www.lumirabeauty.com.au</p>
    </div>
  </section>
</main>
</body>
</html>
```